Brell Harbor Company Business Cards

Front and Back Business Card - logo and text setup - cool design. I need workable photoshop or illustrator files so I can setup each employee card with design that is created
Updates

Hi everyone, thank you for the great entries. Please no more white and blue cards - there are so many already - black and silver only now please. thanks!

Target Market(s)

Construction Industry - Facility Managers

Industry/Entity Type

Construction

Contact Information for Business Card

I really like contemporary simplistic looks - clean neat....not opposed to seeing some black backrounds

Requirements
Must have
• Logo/website address with design on front only - www.brellharbor-example.com (logo attached)
• Back:
• Name/Title/Company Address/Phone/email address
Nice to have
• Cool design
Should not have
• Nothing gimmicky like Fire or Water - since we are a Fire Protection company - it has all been done

```html
<!DOCTYPE html>
<html lang="en">
<head>
<meta charset="utf-8">
<title>Brell Harbor Company Business Cards</title>
<link rel="stylesheet" href="https://fonts.googleapis.com/css2?family=Open+Sans:wght@400;600;700&display=swap">
<style>
  :root {
    --stage-center: #e7e8e9;
    --stage-edge: #d0d1d3;
    --card-white: #ffffff;
    --band-dark: #231f20;
    --band-light: #3d3c3e;
    --ink: #231f20;
    --text-muted: #3a3a3a;
    --brand-navy: #1f3a6e;
    --on-dark: #ffffff;
    --divider: #bdbdbd;
  }
  * { margin: 0; padding: 0; box-sizing: border-box; }
  html, body { width: 800px; height: 1200px; overflow: hidden; }
  body {
    position: relative;
    font-family: "Open Sans", sans-serif;
    background: radial-gradient(ellipse at 50% 50%, var(--stage-center) 0%, var(--stage-edge) 75%);
    border: 1px solid #6d6e70;
  }
  .card { position: absolute; }

  /* Front card */
  .card-front {
    left: 152px; top: 170px; width: 504px; height: 288px;
    background: var(--card-white);
  }
  .name-band {
    position: absolute; left: -4px; top: 22px; width: 504px; height: 80px;
    border-top: 2px solid var(--ink); border-bottom: 2px solid var(--ink);
    padding: 2px 0;
  }
  .name-band-fill {
    width: 100%; height: 100%;
    background: linear-gradient(90deg, var(--band-dark) 0%, var(--band-light) 100%);
    color: var(--on-dark); text-align: center; padding-top: 12px;
  }
  .person-name { font-size: 22px; font-weight: 700; line-height: 1.2; letter-spacing: 0.2px; }
  .person-title { font-size: 12.5px; font-weight: 400; line-height: 1.4; }

  .brand-name-front {
    position: absolute; left: 22px; top: 160px; width: 200px;
    font-size: 20px; font-weight: 700; color: var(--brand-navy); line-height: 1.15;
  }
  .vertical-divider {
    position: absolute; left: 237px; top: 162px; width: 1px; height: 82px;
    background: var(--divider);
  }
  .contact-list { position: absolute; left: 270px; top: 166px; list-style: none; }
  .contact-item {
    display: flex; align-items: center; height: 30px;
    font-size: 12.5px; color: var(--text-muted);
  }
  .contact-item svg { width: 11px; height: 11px; margin-right: 6px; fill: var(--ink); flex-shrink: 0; }
  .contact-item.address svg { width: 12px; height: 13px; margin-right: 9px; }

  /* Back card */
  .card-back {
    left: 148px; top: 704px; width: 504px; height: 286px;
    background: var(--band-dark); color: var(--on-dark); text-align: center;
  }
  .brand-name-back {
    position: absolute; left: 0; right: 0; top: 110px;
    font-size: 28px; font-weight: 700; line-height: 1.1;
  }
  .website { position: absolute; left: 0; right: 0; top: 196px; font-size: 13px; font-weight: 400; }
</style>
</head>
<body>

  <section class="card card-front">
    <div class="name-band">
      <div class="name-band-fill">
        <div class="person-name">Daniel Marsh</div>
        <div class="person-title">Managing Member</div>
      </div>
    </div>

    <div class="brand-name-front">Brell Harbor Company</div>
    <div class="vertical-divider"></div>

    <ul class="contact-list">
      <li class="contact-item phone">
        <svg viewBox="0 0 24 24" aria-hidden="true"><path d="M6.6 10.8a15.1 15.1 0 0 0 6.6 6.6l2.2-2.2c.3-.3.7-.4 1-.2 1.1.4 2.3.6 3.6.6.6 0 1 .4 1 1V20c0 .6-.4 1-1 1A17 17 0 0 1 3 4c0-.6.4-1 1-1h3.5c.6 0 1 .4 1 1 0 1.3.2 2.5.6 3.6.1.3 0 .7-.2 1z"/></svg>
        0300-555-014
      </li>
      <li class="contact-item email">
        <svg viewBox="0 0 24 24" aria-hidden="true"><path d="M2 5h20v14H2z M3.5 6.5 12 13l8.5-6.5" fill="var(--ink)" stroke="#fff" stroke-width="1.5"/></svg>
        @yourweb.com
      </li>
      <li class="contact-item address">
        <svg viewBox="0 0 24 28" aria-hidden="true"><path d="M12 0a10 10 0 0 0-10 10c0 7.5 10 18 10 18s10-10.5 10-18A10 10 0 0 0 12 0zm0 14a4 4 0 1 1 0-8 4 4 0 0 1 0 8z"/></svg>
        your address here
      </li>
    </ul>
  </section>

  <section class="card card-back">
    <div class="brand-name-back">Brell Harbor Company</div>
    <div class="website">www.brellharbor-example.com</div>
  </section>

</body>
</html>
```